Business Card Design Project

Design a business card for a new entity that is in the OTC (over-the-counter-derivative brokering business-Financial Services.
The card should be clean a professional looking. We encourage designers to think pro-actively, fresh and innovative, but also keep in mind that only 2 things are important. a)that the card look professional b)that it is somehow memorable.

We have a new logo which we will upload and will want the Trident symbol in the logo to be raised OR not have the symbol raised and plan on having the word " BROKERAGE SERVICES" raised that stands out and will look sharp.

Along with uploading the new logo which MUST be incorperated, I am also going to upload 3 different business cards of other businesses to use only as guild-lines since I think they are clean and professional looking BUT I encourage all to be pro-active and creative on their own.

Industry/Entity Type

Business

Requirements
Must have
• 1. MUST HAVE THE NEW LOGO WHICH WILL BE UPLOADED
2. MUST HAVE A VERSION SIMILAR TO THE 3 DIFFERENT BUSINESS CARDS I WILL UPLOAD, BUT EACH DESIGNER MUST ONLY THESE THIS FORMAT AS A BACK-UP AND BE CREATIVE ON THEIR OWN FIRST. ALSO WHEN LOOKING AT THE CARDS WHICH I UPLOAD TO USE AS A GUILD-LINE KEEP IN MIND THAT THESE ARE PINNACLE 300 COMPANIES SO DO NOT MIMIC ONLY USE FOR IDEAS.
Nice to have
• these are the 3 different other biz cards to look at for some reference

```html
<!DOCTYPE html>
<html lang="en">
<head>
<meta charset="utf-8">
<title>Keelson Brokerage Services – Stationery</title>
<link rel="stylesheet" href="https://fonts.googleapis.com/css2?family=Arimo:wght@400;700&family=PT+Sans:wght@400;700&display=swap">
<style>
  :root {
    --canvas: #ffffff;
    --paper: #ffffff;
    --ink: #222222;
    --ink-soft: #4a4a4a;
    --rule: #8a8a8a;
    --gold: #e0a91c;
    --gold-deep: #c9961a;
    --gold-light: #f0cb52;
    --charcoal: #2c2c2c;
    --charcoal-light: #3c3c3c;
    --silver: #d8d8d8;
    --mark-dark: #3d3d3d;
  }
  * { margin: 0; padding: 0; box-sizing: border-box; }
  html, body { width: 1200px; height: 900px; overflow: hidden; background: var(--canvas); }
  body { position: relative; font-family: "Arimo", Arial, sans-serif; color: var(--ink); }

  .sheet { position: absolute; background: var(--paper); box-shadow: 3px 4px 8px rgba(0,0,0,.35); }

  /* Letterhead */
  .letterhead { left: 15px; top: 15px; width: 667px; height: 870px; }
  .brand { position: absolute; display: flex; flex-direction: column; align-items: center; font-family: "PT Sans", sans-serif; }
  .brand-dot { width: 22px; height: 22px; border-radius: 50%; background: var(--gold); margin-bottom: 10px; }
  .brand-name { font-weight: 400; letter-spacing: 3px; line-height: 1; text-align: center; }
  .brand-sub { font-weight: 400; letter-spacing: 2.5px; line-height: 1; margin-top: 4px; text-align: center; }
  .letterhead .brand { left: 58px; top: 50px; width: 145px; color: var(--mark-dark); }
  .letterhead .brand-name { font-size: 30px; }
  .letterhead .brand-sub { font-size: 8.5px; }
  .letterhead .brand-dot { margin-bottom: 26px; }
  .office-address { position: absolute; left: 502px; top: 74px; font-size: 10.5px; line-height: 13px; color: var(--ink-soft); }
  .header-rule { position: absolute; left: 222px; top: 140px; width: 393px; height: 1px; background: var(--rule); }
  .watermark { position: absolute; left: 170px; top: 310px; width: 330px; height: 330px; border-radius: 50%; background: #f4f4f4; }
  .signoff { position: absolute; left: 61px; top: 626px; font-size: 11px; line-height: 13px; color: var(--ink); }
  .signoff .closing { margin-bottom: 39px; }
  .letter-sites { position: absolute; left: 0; width: 100%; top: 805px; text-align: center; font-size: 10.5px; color: var(--ink-soft); }
  .letter-sites .sep { color: var(--gold); margin: 0 6px; }
  .member-band { position: absolute; left: 12px; top: 824px; width: 642px; height: 22px; background: linear-gradient(90deg, var(--gold-deep), var(--gold-light) 50%, var(--gold-deep)); font-size: 8px; letter-spacing: .4px; line-height: 22px; text-align: center; color: #5a4510; }

  /* Card front (dark) */
  .card-front { left: 706px; top: 158px; width: 479px; height: 274px; overflow: hidden; background: radial-gradient(ellipse at 50% 55%, var(--charcoal-light), var(--charcoal) 70%); }
  .card-front .brand { left: 0; width: 100%; top: 52px; color: var(--silver); }
  .card-front .brand-dot { margin-bottom: 70px; }
  .card-front .brand-name { font-size: 36px; }
  .card-front .brand-sub { font-size: 11px; letter-spacing: 3px; }
  .front-sites { position: absolute; left: 0; width: 100%; top: 211px; text-align: center; font-family: "PT Sans", sans-serif; font-size: 13px; line-height: 16px; color: #ffffff; }

  /* Card back (white) */
  .card-back { left: 706px; top: 480px; width: 479px; height: 274px; overflow: hidden; }
  .card-back .brand { left: 24px; top: 62px; width: 190px; color: var(--mark-dark); }
  .card-back .brand-dot { margin-bottom: 60px; }
  .card-back .brand-name { font-size: 33px; }
  .card-back .brand-sub { font-size: 10px; letter-spacing: 2.8px; }
  .divider { position: absolute; left: 227px; top: 50px; width: 1px; height: 160px; background: #cfcfcf; }
  .contact { position: absolute; left: 248px; top: 51px; font-family: "PT Sans", sans-serif; color: var(--ink-soft); }
  .contact .person { font-size: 18px; color: var(--gold); line-height: 22px; }
  .contact .role { font-size: 12px; line-height: 15px; margin-bottom: 12px; }
  .contact .line { font-size: 12px; line-height: 16px; display: flex; align-items: center; }
  .contact .line svg { width: 11px; height: 11px; margin-right: 5px; flex: none; }
  .back-members { position: absolute; left: 28px; top: 238px; font-family: "PT Sans", sans-serif; font-size: 9.5px; color: var(--ink-soft); }
  .back-members .dot { color: var(--gold); }
  .back-band { position: absolute; left: 0; bottom: 0; width: 100%; height: 16px; background: linear-gradient(90deg, #2a2a2a, #777 55%, #2a2a2a); }
</style>
</head>
<body>

<section class="sheet letterhead">
  <div class="brand">
    <span class="brand-dot"></span>
    <span class="brand-name">KEELSON</span>
    <span class="brand-sub">BROKERAGE SERVICES</span>
  </div>
  <address class="office-address" style="font-style:normal">
    48 Birchwood Road<br>Suite 310<br>Fairview NJ 07022<br>Main PH: xxx-xxx-xxxx
  </address>
  <div class="header-rule"></div>
  <div class="watermark" role="img" aria-label="Faint company emblem"></div>
  <div class="signoff">
    <p class="closing">Respectfully,</p>
    <p>Alan Pierce / CPO</p>
    <p>Keelson Brokerage Services LLC</p>
    <p>Direct:</p>
    <p>Mobile:</p>
    <p>IM:</p>
  </div>
  <p class="letter-sites">www.KeelsonBrokerageServices.com<span class="sep">|</span>www.KeelsonFutures.com<span class="sep">|</span>www.KeelsonOTC.com</p>
  <p class="member-band">Members of Atlas Exchange Europe · Members of Harbor ClearNet · Members of National Guild of Day Traders</p>
</section>

<section class="sheet card-front">
  <div class="brand">
    <span class="brand-dot"></span>
    <span class="brand-name">KEELSON</span>
    <span class="brand-sub">BROKERAGE SERVICES</span>
  </div>
  <p class="front-sites">www.KeelsonBrokerageServices.com<br>www.KeelsonFutures.com<br>www.KeelsonOTC.com</p>
</section>

<section class="sheet card-back">
  <div class="brand">
    <span class="brand-dot"></span>
    <span class="brand-name">KEELSON</span>
    <span class="brand-sub">BROKERAGE SERVICES</span>
  </div>
  <div class="divider"></div>
  <div class="contact">
    <p class="person">Daniel Marlow</p>
    <p class="role">Principal Consultant</p>
    <p class="line">1870 Cedar Court #205</p>
    <p class="line">Tampa, FL 33609</p>
    <p class="line"><svg viewBox="0 0 12 12"><path d="M2 1h3l1 3-2 1a7 7 0 0 0 3 3l1-2 3 1v3c-6 0-9-3-9-9z" fill="#e0a91c"/></svg>+1 (000) 000 - 0000</p>
    <p class="line"><svg viewBox="0 0 12 12"><rect x="3" y="0.5" width="6" height="11" rx="1" fill="none" stroke="#e0a91c" stroke-width="1.2"/><circle cx="6" cy="9.5" r=".8" fill="#e0a91c"/></svg>+1 (000) 000 - 0000</p>
    <p class="line"><svg viewBox="0 0 12 12"><rect x=".5" y="2.5" width="11" height="7" fill="#e0a91c"/><path d="M.5 2.5 6 7l5.5-4.5" fill="none" stroke="#fff" stroke-width="1"/></svg>dmarlow@KeelsonBrokerageServices.com</p>
    <p class="line"><svg viewBox="0 0 12 12"><circle cx="6" cy="6" r="5.5" fill="#e0a91c"/><path d="M3.5 6h5M6 3.5v5" stroke="#fff" stroke-width="1.3"/></svg>dmarlow@chatline.net</p>
    <p class="line"><svg viewBox="0 0 12 12"><circle cx="6" cy="6" r="5" fill="none" stroke="#e0a91c" stroke-width="1.2"/><path d="M1 6h10M6 1c-3 3-3 7 0 10M6 1c3 3 3 7 0 10" fill="none" stroke="#e0a91c" stroke-width="1"/></svg>www.KeelsonBrokerageServices.com</p>
  </div>
  <p class="back-members">Members of Atlas Exchange Europe <span class="dot">•</span> Members of Harbor ClearNet <span class="dot">•</span> Members of National Guild of Day Traders</p>
  <div class="back-band"></div>
</section>

</body>
</html>
```